Pamphlet Days of the Family - École Mont-Clairval

We * need a pamphlet (flyer) to describe a new project. This project is called "Family Days - École Mont-Clairval". The text describing family days and their intended goals is attached in the downloaded .doc document. We also provided the logo (LE JOURNESS no font in attachment) which represents the school and those days of the family. Please write "Family Days - École Mont-Clairval" on top of the pamphlet with the Logo in plain view (The text The days of the École Mont-Clairval family must be associated with the logo). We need the pamphlet to be colorful, attractive and clean as much as possible. We would like to have childish drawings (see drawing example attached) and photos that represent one or both parents with their child (ren) in a SCHOOL ENVIRONMENT (very important). Parents must feel concerned. It can be a two-sided pamphlet. In color (bright colors as much as possible). The text must be in French so only FRENCH DESIGNERS ARE INVITED to work on this design because the text must remain consistent. The project can be summed up as follows: The Mont-Clairval School wishes to open its doors so that parents can share with their child moments in their student life. They will be invited, at various times of the school year, to participate in the daily life of their child, for example ... • during special activities in class (eg reading, do-it-yourself, job presentation, etc.). events (eg, back to school, Christmas choir, carnival, etc.) • during educational and sports outings (eg skating, library, cinema, etc.) Also, they will have the opportunity to come and spend a period in their child's classroom. They will have the privilege of accompanying him during a usual learning moment. For any additional question, thank you to contact me via this page, it will be my pleasure to answer you quickly. Thank you all for your participation. * We are a committee made up of parents, teachers, school principal, school administrators. Everyone has a say in the final design. So I am only the intermediary responsible for the project. It will be my pleasure to share with you the information received from these different partners for this project.

Target Market(s)

Parents of students at a primary school (ages 5 to 12).

Font styles to use
Sans Serif

Colors

Designer to choose colors to be used in the design.

Requirements
Must have
• The Logo prominently Pamphlet Colorful (beautiful bright colors) Easy to read and understand (some parents speak very little French) Originality (Attractive) Text In French (required) and consistent
Nice to have
• One or more Childish Drawing (s) One (1) parent-child Photo (s) in a school environment Allure Épuré
Should not have
• The Dark Colors Of the Scriptures Too Small A Condensed Text Text English

```html
<!DOCTYPE html>
<html lang="fr">
<head>
<meta charset="utf-8">
<title>Les journées de la famille de Mont-Clairval</title>
<link href="https://fonts.googleapis.com/css2?family=Arimo:wght@400&family=Open+Sans:ital,wght@0,700;1,700&display=swap" rel="stylesheet">
<style>
  :root {
    --page-bg: #ece7df;
    --paper: #ffffff;
    --ink: #231f20;
    --sun: #f6c51b;
    --band-left-a: #fbbf2c;
    --band-left-b: #fde43a;
    --band-mid-a: #f07b31;
    --band-mid-b: #f9c232;
    --band-right-a: #f2d930;
    --band-right-b: #e3e430;
    --photo-a: #c9d889;
    --photo-b: #e8b98a;
    --photo-c: #c8874c;
  }
  html, body {
    margin: 0;
    width: 900px;
    height: 1200px;
    overflow: hidden;
    background: var(--page-bg);
  }
  .flyer {
    position: absolute;
    left: 60px;
    top: 49px;
    width: 690px;
    height: 975px;
    background: var(--paper);
    transform: scale(1.13);
    transform-origin: top left;
    box-shadow: 0 4px 14px rgba(0,0,0,.18);
    overflow: hidden;
    font-family: "Arimo", Arial, sans-serif;
    color: var(--ink);
  }
  .hero-photo {
    position: absolute;
    left: 0; top: 0;
    width: 690px; height: 400px;
    background:
      linear-gradient(180deg, rgba(255,255,255,0) 55%, rgba(200,135,76,.55) 100%),
      linear-gradient(100deg, var(--photo-a) 0%, var(--photo-b) 45%, #dfe3ef 75%, var(--photo-a) 100%);
  }
  .hero-curve {
    position: absolute;
    left: 0; top: 300px;
    width: 690px; height: 110px;
  }
  .kids-drawing {
    position: absolute;
    border: 5px solid #fff;
    box-shadow: 0 2px 6px rgba(0,0,0,.3);
  }
  .kids-drawing.left-back  { left: 28px;  top: 425px; width: 170px; height: 110px; transform: rotate(12deg);  background: linear-gradient(160deg,#6fb24a,#d85a3c 60%,#3b6fb4); }
  .kids-drawing.left-front { left: 25px;  top: 350px; width: 175px; height: 125px; transform: rotate(12deg);  background: linear-gradient(170deg,#cfe6f7 0%,#a6cf6a 45%,#5fa43c 100%); }
  .kids-drawing.right-back { left: 478px; top: 435px; width: 170px; height: 110px; transform: rotate(-14deg); background: linear-gradient(160deg,#cfe9f5,#7cc3e0 60%,#e07c3c); }
  .kids-drawing.right-front{ left: 485px; top: 355px; width: 175px; height: 135px; transform: rotate(-14deg); background: linear-gradient(180deg,#d8eefb 0%,#eef6fb 55%,#7dbf4a 100%); }
  .brand-mark {
    position: absolute;
    left: 286px; top: 368px;
    width: 118px; height: 118px;
    border-radius: 50%;
    background: var(--sun);
  }
  .brand-name {
    position: absolute;
    left: 150px; top: 523px;
    width: 390px;
    margin: 0;
    text-align: center;
    font-family: "Open Sans", Arial, sans-serif;
    font-weight: 700;
    font-size: 18.5px;
    line-height: 24px;
    color: var(--ink);
  }
  .intro {
    position: absolute;
    left: 40px; top: 596px;
    width: 605px;
    font-size: 14.2px;
    line-height: 18.5px;
    text-align: justify;
  }
  .intro p { margin: 0 0 17px; }
  .moments {
    position: absolute;
    left: 0; top: 745px;
    width: 690px; height: 113px;
    display: flex;
  }
  .moment {
    display: flex;
    justify-content: center;
    padding-top: 16px;
    box-sizing: border-box;
    text-align: center;
    font-family: "Open Sans", Arial, sans-serif;
    font-style: italic;
    font-weight: 700;
    font-size: 11.8px;
    line-height: 17px;
  }
  .moment.classroom { width: 235px; background: linear-gradient(135deg, var(--band-left-a), var(--band-left-b)); }
  .moment.events    { width: 218px; background: linear-gradient(200deg, var(--band-mid-b), var(--band-mid-a)); }
  .moment.outings   { width: 237px; background: linear-gradient(135deg, var(--band-right-a), var(--band-right-b)); }
  .closing {
    position: absolute;
    left: 40px; top: 875px;
    width: 605px;
    margin: 0;
    font-size: 14.2px;
    line-height: 18.5px;
    text-align: justify;
  }
</style>
</head>
<body>
  <main class="flyer">
    <div class="hero-photo" role="img" aria-label="Photo d'une mère et de ses deux enfants faisant du bricolage à une table de classe"></div>
    <svg class="hero-curve" viewBox="0 0 690 110" aria-hidden="true">
      <path d="M0 80 Q120 70 250 70 Q262 6 345 2 Q428 6 440 70 Q570 70 690 80 L690 110 L0 110 Z" fill="#ffffff"/>
    </svg>

    <div class="kids-drawing left-back" role="img" aria-label="Dessin d'enfant coloré"></div>
    <div class="kids-drawing left-front" role="img" aria-label="Dessin d'enfant d'un pré fleuri"></div>
    <div class="kids-drawing right-back" role="img" aria-label="Dessin d'enfant coloré"></div>
    <div class="kids-drawing right-front" role="img" aria-label="Dessin d'enfant d'une famille sous un arbre et un soleil"></div>

    <div class="brand-mark" aria-hidden="true"></div>
    <h1 class="brand-name">Les journées de la famille<br>de Mont-Clairval</h1>

    <section class="intro">
      <p>L’école Mont-Clairval souhaite ouvrir ses portes afin que vous puissiez partager avec votre enfant des moments de sa vie d’élève. Vous connaissez votre enfant sous plusieurs de ses facettes. Avec ce projet, vous pourrez maintenant le connaître en tant qu’élève œuvrant dans son milieu scolaire.</p>
      <p>Vous serez invités, à divers moments de l’année scolaire, à participer au quotidien de votre enfant, par exemple…</p>
    </section>

    <section class="moments">
      <div class="moment classroom">lors d’activités<br>spéciales en classe<br>(ex.: lecture, bricolage,<br>présentation de métiers, etc.)</div>
      <div class="moment events">lors d’événements<br>(ex.: la rentrée, chorale de Noël,<br>fête foraine, etc.)</div>
      <div class="moment outings">lors de sorties éducatives<br>et sportives<br>(ex.: patinage, bibliothèque,<br>cinéma, etc.)</div>
    </section>

    <p class="closing">De plus, vous aurez l’opportunité de venir passer une période dans la classe de votre enfant. Vous aurez ainsi le privilège de l’accompagner lors d’un moment d’apprentissage habituel.</p>
  </main>
</body>
</html>
```